Visitenkarten
Zielgruppe
Wir begleiten dich in der Ausbildung, im Studium, bei der Fachwirt-Weiterbildung, damit du deine Prüfungen ohne Hindernisse erfolgreich meisterst.
Aufgabenstellung
Auf der Visitenkarte muss das Logo und folgende Informationen zu sehen sein:
Lernwerkcoach
Timo Brandau
Quaderweg Str. 58
04388 Leipzig
Telefon: 0152 - 3208947
E-Mail: info@lernwerkcoach-beispiel.de
Homepage: www.lernwerkcoach-beispiel.de
sowie einen Link zu meinem Terminvereinbarungskalender: www.terminfix-beispiel.de/lernwerkcoach mit dem Hinweis: „Hier Termin vereinbaren“ (sinngemäße Abwandlung möglich).
Es muss auch ein Hinweis auf eine kostenfreie Probestunde drauf.

```html
<!DOCTYPE html>
<html lang="de">
<head>
<meta charset="utf-8">
<title>Lernwerkcoach – Visitenkarten</title>
<link href="https://fonts.googleapis.com/css2?family=Arimo:wght@400;700&display=swap" rel="stylesheet">
<style>
  :root {
    --teal: #0f4049;
    --teal-text: #174f58;
    --grey-text: #5b6c70;
    --card: #ffffff;
    --backdrop: #2b2b2b;
  }
  * { box-sizing: border-box; margin: 0; padding: 0; }
  html, body { width: 1200px; height: 900px; overflow: hidden; }
  body {
    background: var(--backdrop);
    font-family: "Arimo", Arial, sans-serif;
    position: relative;
  }
  .card {
    position: absolute;
    left: 280px;
    width: 640px;
    height: 400px;
    background: var(--card);
    overflow: hidden;
  }
  .card--front { top: 35px; }
  .card--back { top: 465px; }

  .band {
    position: absolute;
    left: 0; right: 0;
    background: var(--teal);
    color: #fff;
    display: flex;
    align-items: center;
    justify-content: center;
    font-size: 19px;
    letter-spacing: 0.2px;
  }
  .card--front .band { top: 248px; height: 66px; }
  .card--back .band { top: 292px; height: 66px; font-size: 21px; }

  .brand {
    display: flex;
    align-items: center;
    gap: 14px;
    color: var(--teal-text);
    font-weight: 700;
    font-size: 40px;
  }
  .brand__mark {
    width: 34px; height: 34px;
    background: var(--teal);
  }
  .card--front .brand {
    position: absolute;
    top: 92px;
    left: 0; right: 0;
    justify-content: center;
  }

  .back-brand {
    position: absolute;
    left: 40px;
    top: 70px;
    width: 270px;
    display: flex;
    flex-direction: column;
    align-items: center;
    gap: 18px;
    color: var(--teal-text);
    font-weight: 700;
    font-size: 36px;
  }
  .back-brand .brand__mark { width: 40px; height: 40px; }

  .divider {
    position: absolute;
    left: 338px;
    top: 48px;
    width: 2px;
    height: 222px;
    background: var(--teal);
  }

  .contact {
    position: absolute;
    left: 362px;
    top: 44px;
    color: var(--grey-text);
  }
  .contact__name {
    color: var(--teal-text);
    font-weight: 700;
    font-size: 26px;
    letter-spacing: 0.5px;
  }
  .contact__role { font-size: 19px; margin-top: 2px; }
  .contact__address { font-size: 17px; margin-top: 26px; line-height: 1.25; }
  .contact__list { list-style: none; margin-top: 22px; font-size: 17px; }
  .contact__list li {
    display: flex;
    align-items: center;
    gap: 12px;
    height: 27px;
  }
  .contact__list svg { width: 20px; height: 20px; flex: none; }
</style>
</head>
<body>

  <section class="card card--front" aria-label="Vorderseite">
    <div class="brand">
      <span class="brand__mark"></span>
      <span class="brand__name">Lernwerkcoach</span>
    </div>
    <div class="band">Hier Termin vereinbaren: www.terminfix-beispiel.de/lernwerkcoach</div>
  </section>

  <section class="card card--back" aria-label="Rückseite">
    <div class="back-brand">
      <span class="brand__mark"></span>
      <span class="brand__name">Lernwerkcoach</span>
    </div>

    <div class="divider"></div>

    <div class="contact">
      <div class="contact__name">Timo Brandau</div>
      <div class="contact__role">Lernwerkcoach</div>
      <div class="contact__address">Quaderweg Str. 58<br>04388 Leipzig</div>
      <ul class="contact__list">
        <li>
          <svg viewBox="0 0 24 24" aria-hidden="true"><path d="M6.6 10.8a15 15 0 0 0 6.6 6.6l2.2-2.2c.3-.3.7-.4 1-.2 1.1.4 2.3.6 3.6.6.6 0 1 .4 1 1V20c0 .6-.4 1-1 1A17 17 0 0 1 3 4c0-.6.4-1 1-1h3.5c.6 0 1 .4 1 1 0 1.3.2 2.5.6 3.6.1.3 0 .7-.2 1z" fill="#2c3a3d"/></svg>
          <span>0152 - 3208947</span>
        </li>
        <li>
          <svg viewBox="0 0 24 24" aria-hidden="true"><rect x="2.5" y="5" width="19" height="14" fill="none" stroke="#2c3a3d" stroke-width="1.6"/><path d="M2.5 5l9.5 8 9.5-8" fill="none" stroke="#2c3a3d" stroke-width="1.6"/></svg>
          <span>info@lernwerkcoach-beispiel.de</span>
        </li>
        <li>
          <svg viewBox="0 0 24 24" aria-hidden="true"><g fill="none" stroke="#2c3a3d" stroke-width="1.5"><circle cx="12" cy="12" r="9"/><ellipse cx="12" cy="12" rx="4" ry="9"/><path d="M3 12h18M4.5 7.5h15M4.5 16.5h15"/></g></svg>
          <span>www.lernwerkcoach-beispiel.de</span>
        </li>
      </ul>
    </div>

    <div class="band">eine kostenfreie Probestunde drauf</div>
  </section>

</body>
</html>
```